Creative Website Design for Post Production Sound Editorial Company

We are seeking a highly creative and talented web designer to lead the transformation of our existing website into a visually captivating and user-friendly online platform for our Post Production Sound Editorial Company. As a specialized provider of sound editing services for diverse media productions, we recognize the critical importance of a compelling online presence that reflects our expertise and brand identity.
Project Overview:
Our website is already active and hosted via WordPress at https://pagecrate.example/view/velmortaudiocraft.example. Note: The brand book is in the guide. While it serves as a foundation, we are committed to elevating its impact by entrusting you with the task of enhancing its design, functionality, and user experience.

Target Market(s)

* Film Producers: Producers involved in film production, including directors, executive producers, and independent filmmakers, who require high-quality sound editing services to enhance their cinematic projects. * Television Producers: Producers responsible for television shows, series, and documentaries seeking post-production sound editing expertise to improve the audio quality of their content. * Podcast Producers: Podcast creators and producers in need of sound editorial services to enhance the audio experience and professionalism of their podcasts. * Advertising Agencies: Agencies working on multimedia advertising campaigns that require sound editing for commercials, promotional videos, and branded content. * Corporate Video Producers: Professionals responsible for producing corporate videos, training materials, and presentations that require polished and clear audio. * Documentary Filmmakers: Filmmakers creating documentary films who require sound editing to improve the audio clarity and storytelling impact of their projects. * Online Content Creators: Influencers, vloggers, and content creators producing online videos and multimedia content looking to enhance the audio quality of their productions. * Post-Production Studios: Post-production studios that may require specialized sound editing services for their clients, such as major film studios and media companies. * Event Planners: Event planners and organizers who need sound editing for event recordings, promotional videos, and multimedia presentations. * Educational Institutions: Educational institutions, including universities and schools, seeking sound editing services for educational videos, e-learning materials, and multimedia resources. * Government and Nonprofit Organizations: Government agencies and nonprofit organizations in need of sound editing services for public service announcements, informational videos, and awareness campaigns. * Streaming Platforms: Streaming platforms and online content distribution channels that require high-quality sound editing for their content libraries.

Industry/Entity Type

"Media and Entertainment." "Post-Production Services" or "Audio Post-Production Services."

Coding

Coded - Design and coding required

Number of Pages Required

5+ page

Font styles to use
Other font styles liked:
• Nexa

Colors

Designer to choose only greyscale colors for use in the design.

Requirements
Must have
• * Clean and Modern Design: Use a clean and contemporary design with a minimalist aesthetic. This will convey professionalism and make it easy for visitors to navigate our site. * High-Quality Imagery and Multimedia: Incorporate high-resolution images, video clips, and audio samples that showcase our work and expertise. Visual and auditory elements are essential in the sound editing industry. * Color Palette: Use Branding Kit for the color palette * Typography: Use Branding Kit (Nexa) to select clear, legible fonts for easy reading. * Responsive Design: Ensure that the website is fully responsive, adapting seamlessly to various screen sizes and devices. This is crucial for user-friendliness and accessibility. * Intuitive Navigation: Design a user-friendly navigation menu with clear headings and categories. Users should easily find information about our services, portfolio, about the company, and contact details. * Video Backgrounds: Consider using video backgrounds on the homepage or specific sections to capture attention and highlight our expertise. Ensure that the videos are relevant to our services. * Testimonials and Case Studies: Include client testimonials and case studies to build trust and credibility. Showcase successful projects we've worked on and the positive impact our sound editing services have had. * Interactive Elements: Incorporate interactive elements such as buttons, hover effects, and animations to engage visitors and make the website more dynamic. * Call-to-Action (CTA) Buttons: Strategically place CTA buttons throughout the site to encourage visitors to get in touch, request a quote, or explore our portfolio. * Contact Information: Make it easy for visitors to contact us by placing clear contact information, including a contact form, phone number, and email address. * Social Media Integration: Connect your social media profiles to the website to foster engagement and allow visitors to follow your updates. * Accessibility Features: Ensure that the website is accessible to all users, including those with disabilities. This includes using alt text for images and ensuring keyboard navigation is smooth. * Loading Speed: Optimize the website's loading speed to provide a seamless browsing experience. * Security: Implement security measures to protect user data and maintain trust.
Nice to have
• * Testimonials and Case Studies: Include client testimonials and case studies to build trust and credibility. Showcase successful projects you've worked on and the positive impact your sound editing services have had. * Blog Section: Include a blog section where you can share industry insights, tips, and updates. This can position your company as an authority in sound editing.
Should not have
• designers who are inexperienced

```html
<!DOCTYPE html>
<html lang="en">
<head>
<meta charset="utf-8">
<title>Velmort Audiocraft — Website Design</title>
<link rel="stylesheet" href="https://fonts.googleapis.com/css2?family=Outfit:wght@300;400;500;600;700&display=swap">
<style>
:root{
  --page:#f1f1f1;
  --panel:#d4d4d4;
  --panel-light:#e2e2e2;
  --ink:#1f1f1f;
  --ink-soft:#4a4a4a;
  --card:#6f6f6f;
  --card-dark:#4e4e4e;
  --dark:#2f2f2f;
  --line:#8a8a8a;
  --white:#ffffff;
}
*{box-sizing:border-box;margin:0;padding:0}
html,body{width:1200px;height:4080px;overflow:hidden}
body{background:var(--page);font-family:"Outfit",sans-serif;color:var(--ink);position:relative}

.brand-hero{position:absolute;left:255px;top:78px;display:flex;align-items:center;gap:26px}
.brand-hero .mark{width:150px;height:150px;border-radius:50%;background:radial-gradient(circle at 40% 38%,#a9a9a9,#4b4b4b 75%);border:4px solid #d7d7d7}
.brand-hero .name{font-size:58px;font-weight:600;color:#3a3a3a;letter-spacing:-1px}

.panel{position:absolute;left:139px;width:922px;height:518px;overflow:hidden;
  background:radial-gradient(ellipse at 35% 45%,var(--panel-light),var(--panel) 70%)}
.panel .brand{position:absolute;left:82px;top:40px;display:flex;align-items:center;gap:10px}
.panel .brand .dot{width:50px;height:50px;border-radius:50%;background:radial-gradient(circle at 40% 38%,#b0b0b0,#4e4e4e 80%);border:2px solid #e6e6e6}
.panel .brand .name{font-size:18px;font-weight:500;color:#2c2c2c}

.connect{position:absolute;left:790px;top:0;width:140px;height:130px}
.nav{position:absolute;right:45px;top:158px;height:280px;border-right:1.5px solid var(--line);padding-right:20px}
.nav li{list-style:none;height:50px;font-size:9px;font-weight:500;text-align:right;letter-spacing:.4px;color:#333;position:relative;line-height:10px}
.nav li:first-child{margin-top:17px}
.nav li.active{font-weight:700;color:#111}
.nav li.active::after{content:"";position:absolute;right:-22px;top:-10px;width:2.5px;height:30px;background:#222}

.eyebrow{font-size:14px;font-weight:400;color:#222}
.title{font-size:31px;font-weight:400;line-height:33px;color:#111;letter-spacing:-.3px}
.body{font-size:9.5px;line-height:17px;color:var(--ink-soft)}
.btn{display:flex;align-items:center;justify-content:center;gap:10px;height:22px;width:108px;border-radius:3px;font-size:8.5px;font-weight:600;color:#222;
  background:linear-gradient(90deg,#f4f4f4,#ababab);box-shadow:0 2px 4px rgba(0,0,0,.18)}

/* hero */
.hero-copy{position:absolute;left:150px;top:168px;width:270px}
.hero-copy .title{margin-top:6px}
.hero-copy .body{margin-top:10px;line-height:16px}
.hero-copy .btn{margin-top:16px}
.social{position:absolute;left:146px;top:424px;display:flex;gap:17px}
.social span{width:20px;height:20px;border-radius:50%;background:#2f2f2f}
.hero-visual{position:absolute;left:455px;top:115px;width:320px;height:320px;border-radius:50%;
  background:radial-gradient(circle at 50% 50%,#6c6f72 0,#8a8a8a 40%,#bdbdbd 70%,rgba(200,200,200,0) 100%);
  display:flex;align-items:center;justify-content:center}
.play{width:44px;height:44px;border-radius:50%;background:rgba(255,255,255,.25);display:flex;align-items:center;justify-content:center}

/* about */
.about-photo{position:absolute;left:82px;top:122px;width:331px;height:336px;border-radius:4px;
  background:linear-gradient(135deg,#3c3c3c,#8d8d8d 45%,#2a2a2a);box-shadow:0 6px 14px rgba(0,0,0,.3)}
.about-copy{position:absolute;left:446px;top:150px;width:310px}
.about-copy .title{margin-top:6px}
.about-copy .body{margin-top:8px}
.about-copy .btn{margin-top:18px}

.centered{position:absolute;left:0;width:922px;text-align:center}
.centered .btn{margin:0 auto}

/* work */
.work-row{position:absolute;left:150px;top:220px;display:flex;gap:13px}
.work-card{width:198px;text-align:center}
.work-card .poster{height:147px;border-radius:4px}
.work-card .cap{margin-top:12px;font-size:16px;color:#1e1e1e}

/* services */
.service-row{position:absolute;left:150px;top:253px;display:flex;gap:13px}
.service{width:145px;height:119px;border-radius:3px;background:var(--card);display:flex;flex-direction:column;align-items:center;justify-content:center;gap:10px;color:var(--white);font-size:10px}
.service.featured{background:var(--card-dark);box-shadow:0 8px 16px rgba(0,0,0,.35)}

/* testimonial */
.quote-card{position:absolute;left:153px;top:231px;width:279px;height:166px;background:var(--dark);border-radius:3px;color:var(--white);padding:30px 28px 0 28px}
.quote-card p{font-size:8px;line-height:14px}
.quote-card .stars{margin-top:26px;font-size:8px;letter-spacing:1px}
.quote-card .who{font-size:8px;font-weight:700}
.avatar{position:absolute;left:357px;top:382px;width:46px;height:46px;border-radius:50%;border:2px solid #fff;background:linear-gradient(160deg,#9a9a9a,#3c3c3c)}
.pager{position:absolute;left:160px;top:422px}
.globe{position:absolute;left:435px;top:220px;width:320px;height:320px;border-radius:50%;background:radial-gradient(circle at 40% 35%,#ececec,#cfcfcf 70%,#c2c2c2)}
.wave-band{position:absolute;left:0;top:290px;width:922px;height:40px;background:linear-gradient(180deg,transparent,rgba(160,160,160,.35),transparent)}

/* contact + footer */
.rule{position:absolute;left:0;top:303px;width:922px;height:1px;background:#b9b9b9}
.footer{position:absolute;left:150px;top:360px;width:600px;height:140px}
.footer .brand-sm{display:flex;align-items:center;gap:8px;font-size:14px;font-weight:500}
.footer .brand-sm .dot{width:34px;height:34px;border-radius:50%;background:radial-gradient(circle at 40% 38%,#b0b0b0,#4e4e4e 80%)}
.footer .col{position:absolute;font-size:8px;line-height:17px;color:#333}
.footer .divider{position:absolute;top:45px;width:1px;height:80px;background:#9a9a9a}
</style>
</head>
<body>

<header class="brand-hero">
  <div class="mark"></div>
  <div class="name">Velmort Audiocraft</div>
</header>

<!-- HOME -->
<section class="panel" style="top:375px">
  <div class="brand"><span class="dot"></span><span class="name">Velmort Audiocraft</span></div>
  <svg class="connect" viewBox="0 0 140 130"><defs><path id="arc1" d="M100 102 A42 42 0 0 1 100 18"/></defs><text font-size="9" font-weight="700" letter-spacing="3" fill="#222"><textPath href="#arc1">CONNECT US</textPath></text><path d="M92 70 L120 42 M104 42 H120 V58" stroke="#333" stroke-width="1.4" fill="none"/><path d="M112 104 Q128 98 140 88" stroke="#555" fill="none"/></svg>
  <ul class="nav"><li class="active">HOME</li><li>ABOUT</li><li>OUR WORK</li><li>SERVICES</li><li>TESTIMONIALS</li><li>CONTACT</li></ul>

  <div class="hero-copy">
    <div class="eyebrow">Bringing Your Story to</div>
    <h1 class="title">Life Through the<br>Power of Sound</h1>
    <p class="body">Welcome to Velmort Audiocraft, the premier destination for post-production sound editing services. With over 20 years of experience in the industry, our owner brings a wealth of expertise and knowledge to every project.</p>
    <div class="btn">Play Video <svg width="9" height="10" viewBox="0 0 9 10"><path d="M0 0L9 5L0 10Z" fill="#222"/></svg></div>
  </div>
  <div class="social" aria-label="Social links"><span></span><span></span><span></span></div>

  <div class="hero-visual" role="img" aria-label="Showreel video of a sound editor at a studio monitor, framed by a circular audio visual">
    <div class="play"><svg width="20" height="22" viewBox="0 0 20 22"><path d="M2 0L20 11L2 22Z" fill="#fff"/></svg></div>
  </div>
</section>

<!-- ABOUT -->
<section class="panel" style="top:989px">
  <div class="brand"><span class="dot"></span><span class="name">Velmort Audiocraft</span></div>
  <svg class="connect" viewBox="0 0 140 130"><defs><path id="arc2" d="M100 102 A42 42 0 0 1 100 18"/></defs><text font-size="9" font-weight="700" letter-spacing="3" fill="#222"><textPath href="#arc2">CONNECT US</textPath></text><path d="M92 70 L120 42 M104 42 H120 V58" stroke="#333" stroke-width="1.4" fill="none"/><path d="M112 104 Q128 98 140 88" stroke="#555" fill="none"/></svg>
  <ul class="nav"><li>HOME</li><li class="active">ABOUT</li><li>OUR WORK</li><li>SERVICES</li><li>TESTIMONIALS</li><li>CONTACT</li></ul>
  <div class="about-photo" role="img" aria-label="Engineer in headphones working at a mixing console"></div>
  <div class="about-copy">
    <div class="eyebrow">Our Sonic Odyssey</div>
    <h2 class="title">Unveiling the Artistry<br>Behind the Sound</h2>
    <p class="body">Embark on an unforgettable sonic odyssey as we unveil the artistry behind the sound at Velmort Audiocraft. With over 20 years of experience in post-production sound editing, our dedicated team brings expertise, creativity, and a deep understanding of the power of sound to enhance visual storytelling. We are passionate about pushing boundaries, exploring new sonic territories, and crafting immersive audio experiences that captivate audiences. Join us on this sonic adventure as we unravel the secrets behind the art of sound.</p>
    <div class="btn">See More</div>
  </div>
</section>

<!-- OUR WORK -->
<section class="panel" style="top:1604px">
  <div class="brand"><span class="dot"></span><span class="name">Velmort Audiocraft</span></div>
  <svg class="connect" viewBox="0 0 140 130"><defs><path id="arc3" d="M100 102 A42 42 0 0 1 100 18"/></defs><text font-size="9" font-weight="700" letter-spacing="3" fill="#222"><textPath href="#arc3">CONNECT US</textPath></text><path d="M92 70 L120 42 M104 42 H120 V58" stroke="#333" stroke-width="1.4" fill="none"/><path d="M112 104 Q128 98 140 88" stroke="#555" fill="none"/></svg>
  <ul class="nav"><li>HOME</li><li>ABOUT</li><li class="active">OUR WORK</li><li>SERVICES</li><li>TESTIMONIALS</li><li>CONTACT</li></ul>
  <div class="centered" style="top:104px">
    <div class="eyebrow" style="font-size:13px">Sonic Showreel</div>
    <h2 class="title" style="margin-top:6px">Where Creativity<br>Finds its Sonic Voice</h2>
  </div>
  <div class="work-row">
    <div class="work-card"><div class="poster" role="img" aria-label="Film poster for Crown Of The Valley" style="background:linear-gradient(135deg,#2a2a2a,#9c9c9c 50%,#1e1e1e)"></div><div class="cap">Crown Of The Valley</div></div>
    <div class="work-card"><div class="poster" role="img" aria-label="Film poster for Flicks Warden" style="background:linear-gradient(160deg,#bdbdbd,#555 55%,#1c1c1c)"></div><div class="cap">Flicks Warden</div></div>
    <div class="work-card"><div class="poster" role="img" aria-label="Series poster for The Projections" style="background:linear-gradient(135deg,#5a5a5a,#a8a8a8 40%,#2e2e2e)"></div><div class="cap">The Projections</div></div>
  </div>
  <div class="centered" style="top:422px"><div class="btn">See More</div></div>
</section>

<!-- SERVICES -->
<section class="panel" style="top:2218px">
  <div class="brand"><span class="dot"></span><span class="name">Velmort Audiocraft</span></div>
  <svg class="connect" viewBox="0 0 140 130"><defs><path id="arc4" d="M100 102 A42 42 0 0 1 100 18"/></defs><text font-size="9" font-weight="700" letter-spacing="3" fill="#222"><textPath href="#arc4">CONNECT US</textPath></text><path d="M92 70 L120 42 M104 42 H120 V58" stroke="#333" stroke-width="1.4" fill="none"/><path d="M112 104 Q128 98 140 88" stroke="#555" fill="none"/></svg>
  <ul class="nav"><li>HOME</li><li>ABOUT</li><li>OUR WORK</li><li class="active">SERVICES</li><li>TESTIMONIALS</li><li>CONTACT</li></ul>
  <div class="centered" style="top:130px">
    <div class="eyebrow" style="font-size:13px">Sonic Alchemy</div>
    <h2 class="title" style="margin-top:6px">Transforming Sound into<br>Captivating Experiences</h2>
  </div>
  <div class="service-row">
    <div class="service">
      <svg width="38" height="36" viewBox="0 0 38 36" fill="#fff"><rect x="2" y="2" width="15" height="10" rx="2"/><rect x="21" y="2" width="15" height="10" rx="2"/><circle cx="10" cy="20" r="4"/><circle cx="28" cy="20" r="4"/><path d="M2 34a8 7 0 0 1 16 0Z M20 34a8 7 0 0 1 16 0Z"/></svg>
      Dialogue Editing</div>
    <div class="service featured">
      <svg width="40" height="24" viewBox="0 0 40 24" stroke="#fff" stroke-width="1.6" stroke-linecap="round"><path d="M2 12v0M6 9v6M10 6v12M14 10v4M18 3v18M22 7v10M26 4v16M30 9v6M34 6v12M38 11v2"/></svg>
      Sound Effects Editing</div>
    <div class="service">
      <svg width="36" height="36" viewBox="0 0 36 36" fill="none" stroke="#fff" stroke-width="2"><rect x="2" y="2" width="32" height="32" rx="3"/><path d="M11 7v22M18 7v22M25 7v22"/><rect x="8" y="11" width="6" height="4" fill="#fff"/><rect x="15" y="20" width="6" height="4" fill="#fff"/><rect x="22" y="14" width="6" height="4" fill="#fff"/></svg>
      foley editing</div>
    <div class="service">
      <svg width="38" height="34" viewBox="0 0 38 34" fill="none" stroke="#fff" stroke-width="2"><rect x="2" y="2" width="34" height="30" rx="4"/><circle cx="12" cy="14" r="6"/><circle cx="26" cy="14" r="6"/><path d="M8 26h22"/></svg>
      ADR Editing And Mixing</div>
  </div>
  <div class="centered" style="top:422px"><div class="btn">See More</div></div>
</section>

<!-- TESTIMONIALS -->
<section class="panel" style="top:2832px">
  <div class="wave-band"></div>
  <div class="globe" role="img" aria-label="Dotted world globe illustration"></div>
  <div class="brand"><span class="dot"></span><span class="name">Velmort Audiocraft</span></div>
  <svg class="connect" viewBox="0 0 140 130"><defs><path id="arc5" d="M100 102 A42 42 0 0 1 100 18"/></defs><text font-size="9" font-weight="700" letter-spacing="3" fill="#222"><textPath href="#arc5">CONNECT US</textPath></text><path d="M92 70 L120 42 M104 42 H120 V58" stroke="#333" stroke-width="1.4" fill="none"/><path d="M112 104 Q128 98 140 88" stroke="#555" fill="none"/></svg>
  <ul class="nav"><li>HOME</li><li>ABOUT</li><li>OUR WORK</li><li>SERVICES</li><li class="active">TESTIMONIALS</li><li>CONTACT</li></ul>
  <div style="position:absolute;left:152px;top:130px">
    <div class="eyebrow" style="font-size:13px">Our Testimonials</div>
    <h2 class="title" style="margin-top:4px">What Our Client Says</h2>
  </div>
  <div class="quote-card">
    <p>Lorem Ipsum is simply dummy text of the printing and typesetting industry. Lorem Ipsum has been the industry's standard dummy text ever since the 1500s, when an unknown printer took a galley of type and scrambled</p>
    <div class="stars">★★★★★</div>
    <div class="who">MARCUS - MD</div>
  </div>
  <div class="avatar" role="img" aria-label="Client portrait"></div>
  <svg class="pager" width="70" height="12" viewBox="0 0 70 12"><path d="M6 6H64" stroke="#333"/><circle cx="6" cy="6" r="4.5" fill="#222"/><circle cx="35" cy="6" r="3" fill="#222"/><circle cx="64" cy="6" r="3" fill="#222"/></svg>
</section>

<!-- CONTACT -->
<section class="panel" style="top:3446px">
  <div class="brand"><span class="dot"></span><span class="name">Velmort Audiocraft</span></div>
  <svg class="connect" viewBox="0 0 140 130"><defs><path id="arc6" d="M100 102 A42 42 0 0 1 100 18"/></defs><text font-size="9" font-weight="700" letter-spacing="3" fill="#222"><textPath href="#arc6">CONNECT US</textPath></text><path d="M92 70 L120 42 M104 42 H120 V58" stroke="#333" stroke-width="1.4" fill="none"/><path d="M112 104 Q128 98 140 88" stroke="#555" fill="none"/></svg>
  <ul class="nav"><li>HOME</li><li>ABOUT</li><li>OUR WORK</li><li>SERVICES</li><li>TESTIMONIALS</li><li class="active">CONTACT</li></ul>
  <div class="rule"></div>
  <div class="centered" style="top:114px">
    <div class="eyebrow" style="font-size:13px">Sonic Connection</div>
    <h2 class="title" style="margin-top:6px">Let's Craft Sonic Magic<br>Together</h2>
    <p class="body" style="width:560px;margin:12px auto 0;line-height:17px">We believe in the power of collaboration and the magic that can be created when passionate individuals come together. Get in touch with our team at Velmort Audiocraft and let's embark on a sonic journey together. Whether you're a filmmaker, or any creative professional seeking to elevate your project with outstanding sound, we are here to listen, understand your vision, and bring it to life through our expertise in post-production sound editing.</p>
    <div class="btn" style="margin-top:12px">Contact Us</div>
  </div>
  <footer class="footer">
    <div class="brand-sm"><span class="dot"></span>Velmort Audiocraft</div>
    <p class="col" style="left:0;top:48px;width:165px">Let's collaborate and craft sonic magic that will captivate and resonate with your audience. Reach out to us today and let the sonic adventure begin.</p>
    <div class="divider" style="left:228px"></div>
    <p class="col" style="left:270px;top:48px;width:110px;text-align:center">Home<br>About<br>Our Work<br>Services<br>Contact Us</p>
    <div class="divider" style="left:418px"></div>
    <p class="col" style="left:492px;top:48px;width:140px">© 2023 Velmort Audiocraft All rights reserved Terms and Privacy Policy</p>
  </footer>
</section>

</body>
</html>
```